Business card for utility of the future

I need a business card template designed for brookvane. We provide sustainable water, energy and waste services to homes.

The card should include name, position, email address, phone number, website and our logo (attached). I would like it to convey professionalism and creativity.

Target Market(s)

Homeowners, investors, corporate partners.

Industry/Entity Type

Utility

Contact Information for Business Card

The card should include name, position, email address, phone number, website and our logo (attached).

```html
<!DOCTYPE html>
<html lang="en">
<head>
<meta charset="utf-8">
<title>brookvane business card</title>
<link href="https://fonts.googleapis.com/css2?family=Nunito:wght@800&family=Source+Sans+3:wght@400&display=swap" rel="stylesheet">
<style>
  :root {
    --backdrop: #e9e6e3;
    --card-dark: #58585a;
    --card-light: #ffffff;
    --brand-green: #6fc285;
    --accent-coral: #ec8665;
    --ink: #58585a;
  }
  html, body {
    margin: 0;
    width: 1200px;
    height: 1200px;
    overflow: hidden;
    background: var(--backdrop);
  }
  .card {
    position: absolute;
    left: 215px;
    width: 770px;
    height: 436px;
    border-radius: 24px;
    overflow: hidden;
    box-shadow: 0 6px 14px rgba(0,0,0,0.25);
  }
  .card--front { top: 133px; background: var(--card-dark); }
  .card--back  { top: 632px; background: var(--card-light); }

  .wordmark {
    position: absolute;
    font-family: "Nunito", sans-serif;
    font-weight: 800;
    color: var(--brand-green);
    letter-spacing: -0.02em;
    line-height: 1;
    white-space: nowrap;
  }
  .card--front .wordmark { left: 50%; top: 168px; transform: translateX(-50%); font-size: 92px; }
  .card--back .wordmark { right: 58px; top: 46px; font-size: 64px; }

  .contact {
    position: absolute;
    left: 59px;
    top: 228px;
    font-family: "Source Sans 3", sans-serif;
    color: var(--ink);
  }
  .contact__name { margin: 0; font-size: 29px; color: var(--brand-green); font-weight: 400; line-height: 1.1; }
  .contact__role { margin: 2px 0 0; font-size: 19px; }
  .contact__list { list-style: none; margin: 12px 0 0; padding: 0; font-size: 20px; }
  .contact__list li { display: flex; align-items: center; height: 26px; }
  .contact__icon { width: 17px; height: 17px; margin-right: 13px; fill: var(--accent-coral); }

  .card__band { position: absolute; left: 0; bottom: 0; width: 770px; height: 46px; }
</style>
</head>
<body>
  <section class="card card--front">
    <div class="wordmark">brookvane</div>
  </section>

  <section class="card card--back">
    <div class="wordmark">brookvane</div>

    <div class="contact">
      <h1 class="contact__name">Daniel Hart</h1>
      <p class="contact__role">Managing Partner</p>
      <ul class="contact__list">
        <li>
          <svg class="contact__icon" viewBox="0 0 20 20" aria-hidden="true">
            <path d="M2 7c0-3 4-4 8-4s8 1 8 4v1h-4V6H6v2H2z"/>
            <rect x="4" y="9" width="12" height="8" rx="1.5"/>
            <circle cx="10" cy="13" r="2" fill="#fff"/>
          </svg>
          +00 000-0000
        </li>
        <li>
          <svg class="contact__icon" viewBox="0 0 20 20" aria-hidden="true">
            <rect x="1" y="4" width="18" height="12"/>
            <path d="M1 4l9 7 9-7M1 16l7-6M19 16l-7-6" stroke="#fff" stroke-width="1.4" fill="none"/>
          </svg>
          daniel@brookvane.com
        </li>
        <li>
          <svg class="contact__icon" viewBox="0 0 20 20" aria-hidden="true">
            <g fill="none" stroke="#ec8665" stroke-width="1.3">
              <circle cx="10" cy="10" r="8"/>
              <ellipse cx="10" cy="10" rx="3.5" ry="8"/>
              <path d="M2 10h16M3.5 6h13M3.5 14h13"/>
            </g>
          </svg>
          www.brookvane.com
        </li>
      </ul>
    </div>

    <svg class="card__band" viewBox="0 0 770 46" aria-hidden="true">
      <rect x="0" y="31" width="320" height="15" fill="var(--brand-green)"/>
      <polygon points="318,46 360,46 401,0 361,0" fill="var(--accent-coral)"/>
      <polygon points="367,46 770,46 770,0 407,0" fill="var(--brand-green)"/>
    </svg>
  </section>
</body>
</html>
```